Business card - mobile service

O KiraVox is a mobile family safety service based on tablets and smartphones.
The business card must have:
BASIC INFO
Company Logo
Name
Position / Job Title: Co-founder
Mobile Phone Number: +55 (11) 5830 9172
Land Line: +55 (11) 8761 203945
Email Address: name@kiravox-example.com
Web Site URL: www.kiravox-example.com
PROMOTIONAL INFO
Try KiraVox free Today!
Your personal promo code: qqqq-5839-wwww-4162-9087
Promo code text explanation with the instructions about the trial offer
Updates
Dears,
One more must have: the KiraVox slogan:
Safety

```html
<!DOCTYPE html>
<html lang="en">
<head>
<meta charset="utf-8">
<title>KiraVox business card</title>
<link rel="stylesheet" href="https://fonts.googleapis.com/css2?family=Varela+Round&display=swap">
<style>
  :root {
    --sky: #1fa9e6;
    --sky-deep: #0f93d4;
    --sky-pale: #bfe7f8;
    --sun: #ffd21a;
    --sun-deep: #f0b800;
    --paper: #ffffff;
    --label: #d4effb;
    --stage: #f2f2f2;
  }
  * { margin: 0; padding: 0; box-sizing: border-box; }
  html, body { width: 1200px; height: 900px; overflow: hidden; }
  body {
    background: var(--stage);
    font-family: "Varela Round", "DejaVu Sans", sans-serif;
    position: relative;
  }
  .card {
    position: absolute;
    left: 280px;
    width: 640px;
    height: 366px;
    background: var(--paper);
    overflow: hidden;
    box-shadow: 0 4px 14px rgba(0,0,0,0.12);
  }
  .card--front { top: 56px; }
  .card--back { top: 478px; }

  .brand { position: absolute; color: var(--sky); letter-spacing: 0.5px; }
  .slogan { position: absolute; color: var(--sun-deep); font-size: 14px; letter-spacing: 2px; text-transform: uppercase; }

  /* front */
  .front-art { position: absolute; inset: 0; }
  .card--front .brand { left: 34px; top: 118px; font-size: 40px; }
  .card--front .slogan { left: 36px; top: 168px; }
  .holder { position: absolute; right: 36px; top: 30px; text-align: right; }
  .holder__name { color: var(--sky); font-size: 30px; }
  .holder__role { color: var(--sun-deep); font-size: 14px; margin-top: 2px; }
  .contacts {
    position: absolute;
    left: 300px; top: 162px;
    display: grid;
    grid-template-columns: 96px auto;
    row-gap: 6px;
    align-items: baseline;
  }
  .contacts__label { color: var(--label); font-size: 10px; }
  .contacts__value { color: var(--paper); font-size: 16px; }
  .website {
    position: absolute;
    right: 36px; top: 256px;
    color: var(--paper);
    font-size: 22px;
  }

  /* back */
  .rays {
    position: absolute; left: 0; top: 0;
    width: 100%; height: 190px;
    background: radial-gradient(ellipse at 50% 100%, var(--paper) 20%, var(--sky-pale) 60%, #dff3fb 100%);
  }
  .sun-field {
    position: absolute; left: 0; top: 170px;
    width: 100%; height: 196px;
    background: var(--sun);
  }
  .badge {
    position: absolute;
    left: 200px; top: 30px;
    width: 240px; height: 156px;
    border-radius: 50%;
    background: var(--paper);
  }
  .card--back .brand { left: 0; right: 0; top: 66px; text-align: center; font-size: 44px; }
  .card--back .slogan { left: 0; right: 0; top: 124px; text-align: center; }
  .promo { position: absolute; left: 0; right: 0; top: 200px; text-align: center; color: var(--sky); }
  .promo__headline { font-size: 26px; }
  .promo__code { font-size: 15px; margin-top: 10px; }
  .promo__code strong { font-weight: normal; letter-spacing: 0.5px; }
  .promo__note { font-size: 11px; margin: 10px auto 0; width: 440px; line-height: 1.5; color: var(--sky-deep); }
</style>
</head>
<body>

<section class="card card--front" aria-label="Business card front">
  <svg class="front-art" viewBox="0 0 640 366" width="640" height="366" aria-hidden="true">
    <defs>
      <linearGradient id="frontBlue" x1="0" y1="0" x2="1" y2="1">
        <stop offset="0" stop-color="#3fbdf0"/>
        <stop offset="1" stop-color="#1aa3e2"/>
      </linearGradient>
    </defs>
    <path d="M0 205 C 200 185, 350 112, 640 100 L640 366 L0 366 Z" fill="url(#frontBlue)"/>
    <path d="M0 208 C 200 188, 350 115, 640 103" fill="none" stroke="#ffd21a" stroke-width="3"/>
  </svg>
  <p class="brand">KiraVox</p>
  <p class="slogan">Safety</p>
  <div class="holder">
    <p class="holder__name">Lucas Moretti</p>
    <p class="holder__role">Co-founder</p>
  </div>
  <dl class="contacts">
    <dt class="contacts__label">Mobile Phone</dt><dd class="contacts__value">+55 (11) 5830 9172</dd>
    <dt class="contacts__label">Land Line</dt><dd class="contacts__value">+55 (11) 8761 203945</dd>
    <dt class="contacts__label">Email</dt><dd class="contacts__value">name@kiravox-example.com</dd>
  </dl>
  <p class="website">www.kiravox-example.com</p>
</section>

<section class="card card--back" aria-label="Business card back">
  <div class="rays" role="img" aria-label="Light blue sunburst rays radiating from the name"></div>
  <div class="sun-field"></div>
  <div class="badge"></div>
  <p class="brand">KiraVox</p>
  <p class="slogan">Safety</p>
  <div class="promo">
    <p class="promo__headline">Try KiraVox free Today!</p>
    <p class="promo__code">Your personal promo code: <strong>qqqq-5839-wwww-4162-9087</strong></p>
    <p class="promo__note">Enter this code in the KiraVox app to start your free 30-day trial. Valid for one new account only.</p>
  </div>
</section>

</body>
</html>
```